The Gemstone Craft Studio Sales Business Card

The goal of this project is to create a interactive & effective business card design for SALES purposes with the intention to get customer on to our website and make a purchase or contact us about a product or service.
Website: WWW.FENWORKSHOP.COM
LocalListPro: https://lcl.page/FenWORKSHOP?gm
Pagebook & Snapgrid: @THEBRIMORECRAFTSTUDIO
Phone # & Text Message & Chatwire Message: +1(555) 418-2963
Email: HELLO@FENWORKSHOP.COM
Location: 2871 Marbury Lane Suite 412 Harwick Vale, KT
(It would be necessary to have the appropriate ticker/icon for each social media platform as well as the location ticker and phone / messaging icons instead of spelling the words out.)
It is important to have the company logo and details but with an emphasis toward website. Feel free to also completely make one design your way and completely custom as you feel best.
The Gemstone Craft Studio is a Provider of Luxury Goods & Services such as: Custom Jewelry Design, Jewelry Repairs & Cleaning, Designer Jewelry, Luxury Gifts, 24 Karat Gold, 22 Karat Gold Jewelry, Diamond Jewelry, Insured Jewelry Appraisals, Loose Gemstones & Diamonds, Supporting Sustainability
Target Market(s)
People looking to invest in precious metals and gemstones as well as people looking to find a gift for a loved one for a special occasion. Customers looking to Custom Design Jewelry.
Contact Information for Business Card
Font styles to use
Other font styles liked:
- w.e you want
Colors
Designer to choose colors to be used in the design.
Requirements
Must have
- Website: WWW.FENWORKSHOP.COM
- LocalListPro: https://lcl.page/FenWORKSHOP?gm
- Pagebook & Snapgrid: @THEBRIMORECRAFTSTUDIO
- Phone # & Text Message & Chatwire Message: +1(555) 418-2963
- Email: HELLO@FENWORKSHOP.COM
- Location: 2871 Marbury Lane Suite 412 Harwick Vale, KT
- (It would be necessary to have the appropriate ticker/icon for each social media platform as well as the location ticker and phone / messaging icons instead of spelling the words out.)
- It is important to have the company logo and details but with an emphasis toward website. Feel free to also completely make one design your way and completely custom as you feel best.
Nice to have
- The Gemstone Craft Studio is a Provider of Luxury Goods & Services such as: Custom Jewelry Design, Jewelry Repairs & Cleaning, Designer Jewelry, Luxury Gifts, 24 Karat Gold, 22 Karat Gold Jewelry, Diamond Jewelry, Insured Jewelry Appraisals, Loose Gemstones & Diamonds, Supporting Sustainability

```html
<!DOCTYPE html>
<html lang="en">
<head>
<meta charset="utf-8">
<title>The Gemstone Craft Studio – Business Card</title>
<link href="https://fonts.googleapis.com/css2?family=Carlito:wght@400;700&family=Cinzel:wght@400;700&display=swap" rel="stylesheet">
<style>
  :root {
    --charcoal: #3f3f41;
    --red: #ec1f28;
    --red-deep: #7a0008;
    --yellow: #fdd043;
    --yellow-dark: #e2b52a;
    --white: #ffffff;
    --blue: #1479c4;
    --sans: "Carlito", "Calibri", sans-serif;
    --serif: "Cinzel", serif;
  }
  * { margin: 0; padding: 0; box-sizing: border-box; }
  html, body { width: 1200px; height: 686px; overflow: hidden; background: var(--charcoal); }
  .card { position: relative; width: 1200px; height: 686px; background: var(--charcoal); overflow: hidden; font-family: var(--sans); color: var(--white); }

  .brand-panel { position: absolute; left: 0; top: 0; width: 490px; height: 686px; background: var(--charcoal); }
  .brand-mark { position: absolute; left: 175px; top: 190px; width: 140px; height: 140px; border-radius: 50%; background: var(--yellow); }
  .brand-name { position: absolute; left: 0; top: 372px; width: 490px; text-align: center; font-family: var(--serif); font-weight: 700; color: var(--red); font-size: 40px; line-height: 48px; letter-spacing: 1px; }

  .accent-strip { position: absolute; left: 490px; width: 39px; background: var(--yellow); }
  .accent-strip.top { top: 0; height: 101px; }
  .accent-strip.bottom { top: 587px; height: 99px; }
  .divider { position: absolute; left: 490px; top: 101px; width: 1px; height: 486px; background: #2a2a2b; }

  .contact-panel { position: absolute; left: 529px; top: 0; width: 578px; height: 686px; background: var(--red); }
  .band-shadow { position: absolute; left: 529px; top: 381px; width: 578px; height: 60px; background: linear-gradient(to bottom, var(--red-deep), rgba(236,31,40,0)); }
  .band-fold { position: absolute; left: 491px; top: 381px; }

  .web-band { position: absolute; left: 491px; top: 251px; width: 646px; height: 130px; background: var(--yellow); box-shadow: 14px 6px 30px rgba(0,0,0,.55); }
  .globe-badge { position: absolute; left: 17px; top: 24px; width: 76px; height: 76px; border-radius: 50%; background: var(--charcoal); display: flex; align-items: center; justify-content: center; }
  .web-pill { position: absolute; left: 111px; top: 30px; width: 513px; height: 64px; border-radius: 10px; background: var(--charcoal); display: flex; align-items: center; justify-content: center; font-size: 42px; letter-spacing: 1px; color: var(--white); }

  .line { position: absolute; left: 529px; width: 578px; text-align: center; white-space: nowrap; }
  .label-chip { display: inline-flex; align-items: center; gap: 6px; font-size: 20px; font-weight: 700; color: var(--white); }
  .chip-square { width: 14px; height: 14px; background: var(--white); display: inline-block; }
  .listing-label { top: 22px; }
  .listing-url { top: 74px; font-size: 36px; }
  .social-labels { top: 132px; }
  .social-labels .label-chip { margin: 0 10px; }
  .handle { top: 178px; font-size: 36px; }
  .talk-icons { top: 393px; display: flex; justify-content: center; align-items: center; gap: 14px; }
  .phone { top: 446px; font-size: 33px; }
  .mail-icon { top: 494px; }
  .email { top: 536px; font-size: 33px; }
  .pin-icon { top: 578px; }
  .address { top: 632px; font-size: 23px; }
</style>
</head>
<body>
<main class="card">
  <section class="brand-panel">
    <div class="brand-mark"></div>
    <h1 class="brand-name">THE GEMSTONE<br>CRAFT STUDIO</h1>
  </section>

  <div class="accent-strip top"></div>
  <div class="divider"></div>
  <div class="accent-strip bottom"></div>

  <section class="contact-panel"></section>
  <div class="band-shadow"></div>
  <svg class="band-fold" width="38" height="42" viewBox="0 0 38 42"><polygon points="0,0 38,0 38,42" fill="var(--yellow-dark)"/></svg>

  <div class="web-band">
    <div class="globe-badge">
      <svg width="50" height="50" viewBox="0 0 50 50" fill="none" stroke="#fff" stroke-width="2.4">
        <circle cx="25" cy="25" r="21" fill="var(--charcoal)"/>
        <ellipse cx="25" cy="25" rx="9" ry="21"/>
        <line x1="25" y1="4" x2="25" y2="46"/>
        <line x1="6" y1="15" x2="44" y2="15"/>
        <line x1="6" y1="35" x2="44" y2="35"/>
        <rect x="4" y="20" width="42" height="10" fill="#fff" stroke="none"/>
        <text x="25" y="28.5" text-anchor="middle" font-family="Carlito, sans-serif" font-size="9" fill="var(--charcoal)" stroke="none">WWW</text>
      </svg>
    </div>
    <div class="web-pill">WWW.FENWORKSHOP.COM</div>
  </div>

  <div class="line listing-label"><span class="label-chip"><span class="chip-square"></span>LocalListPro</span></div>
  <div class="line listing-url">https://lcl.page/FenWORKSHOP?gm</div>
  <div class="line social-labels"><span class="label-chip">Pagebook</span><span class="label-chip">Snapgrid</span></div>
  <div class="line handle">@thebrimorecraftstudio</div>

  <div class="line talk-icons">
    <svg width="46" height="46" viewBox="0 0 46 46" fill="#fff">
      <path d="M8 4c3-2 6 0 8 4l3 6c1 2 0 4-2 5l-3 2c2 5 6 9 11 11l2-3c1-2 3-3 5-2l6 3c4 2 5 5 3 8l-3 4c-2 3-7 3-12 1C17 38 8 29 4 20 2 14 3 9 6 6z"/>
      <path d="M28 6a12 12 0 0 1 12 12M28 12a6 6 0 0 1 6 6" fill="none" stroke="#fff" stroke-width="2.4" stroke-linecap="round"/>
    </svg>
    <svg width="50" height="44" viewBox="0 0 50 44">
      <path d="M4 2h42a3 3 0 0 1 3 3v26a3 3 0 0 1-3 3H20l-10 9v-9H4a3 3 0 0 1-3-3V5a3 3 0 0 1 3-3z" fill="#fff"/>
      <circle cx="15" cy="18" r="2.6" fill="var(--red)"/><circle cx="25" cy="18" r="2.6" fill="var(--red)"/><circle cx="35" cy="18" r="2.6" fill="var(--red)"/>
    </svg>
    <span class="label-chip">Chatwire</span>
  </div>
  <div class="line phone">+1(555) 418-2963</div>

  <div class="line mail-icon">
    <svg width="44" height="42" viewBox="0 0 44 42">
      <rect x="1" y="1" width="42" height="40" rx="8" fill="#fff"/>
      <rect x="8" y="11" width="28" height="20" rx="2" fill="var(--red)"/>
      <path d="M8 12l14 11 14-11" fill="none" stroke="#fff" stroke-width="2.4"/>
    </svg>
  </div>
  <div class="line email">Hello@fenworkshop.com</div>

  <div class="line pin-icon">
    <svg width="40" height="52" viewBox="0 0 40 52">
      <path d="M20 1C9 1 1 9 1 19c0 12 19 32 19 32s19-20 19-32C39 9 31 1 20 1z" fill="var(--blue)"/>
      <circle cx="20" cy="18" r="7" fill="#fff"/>
    </svg>
  </div>
  <div class="line address">2871 Marbury Lane Suite 412 Harwick Vale, KT</div>
</main>
</body>
</html>
```